Simple elegant business card

General card for a fin and television director.
Just want name, email, phone and address.

Target Market(s)

Prospective employers

Industry/Entity Type

Business

Requirements
Must have
• As above
Nice to have
• Logo but not necessary.
Should not have
• Not too colourful or funky.
• Simplicity and elegance the way to go.

```html
<!DOCTYPE html>
<html lang="en">
<head>
<meta charset="utf-8">
<title>Nora Hale — Business Card</title>
<link rel="stylesheet" href="https://fonts.googleapis.com/css2?family=Josefin+Sans:wght@300&family=Cormorant+Garamond:ital,wght@1,500&display=swap">
<style>
  :root {
    --page-bg: #e9e6e1;
    --card-bg: #1c1c1d;
    --gold: #cfae63;
    --gold-soft: rgba(207, 174, 99, 0);
  }
  html, body {
    margin: 0;
    width: 1200px;
    height: 1000px;
    overflow: hidden;
    background: var(--page-bg);
  }
  .business-card {
    position: absolute;
    left: 80px;
    top: 217px;
    width: 1040px;
    height: 566px;
    background: var(--card-bg);
    box-shadow: 0 10px 30px rgba(0, 0, 0, 0.18);
  }
  .identity {
    position: absolute;
    left: 66px;
    top: 383px;
    width: 370px;
    color: var(--gold);
  }
  .identity__name {
    margin: 0;
    font-family: "Josefin Sans", sans-serif;
    font-weight: 300;
    font-size: 66px;
    line-height: 1;
    letter-spacing: 0.5px;
    white-space: nowrap;
  }
  .identity__title {
    margin: 4px 0 0;
    text-align: right;
    font-family: "Cormorant Garamond", serif;
    font-style: italic;
    font-weight: 500;
    font-size: 26px;
    line-height: 1;
    letter-spacing: 1px;
  }
  .divider {
    position: absolute;
    left: 518px;
    top: 362px;
    width: 2px;
    height: 154px;
    background: linear-gradient(to bottom, var(--gold-soft), var(--gold) 25%, var(--gold) 75%, var(--gold-soft));
  }
  .contact {
    position: absolute;
    left: 586px;
    top: 377px;
    margin: 0;
    padding: 0;
    list-style: none;
    font-family: "Josefin Sans", sans-serif;
    font-weight: 300;
    font-size: 22px;
    line-height: 40.5px;
    letter-spacing: 0.6px;
    color: var(--gold);
  }
</style>
</head>
<body>
  <article class="business-card">
    <div class="identity">
      <h1 class="identity__name">Nora Hale</h1>
      <p class="identity__title">Director</p>
    </div>
    <div class="divider"></div>
    <ul class="contact">
      <li class="contact__phone">+1 310 555 0142</li>
      <li class="contact__address">P.O. Box 418 Ambergate 4410 Qld</li>
      <li class="contact__email">norahale@mail.com</li>
    </ul>
  </article>
</body>
</html>
```